Looking for an Innovative Print Design (Service Directory)

We need a new design for our advertisement within a printed colour services directory.

We are a compensation law firm called Velbrook Compensation Lawyers. Feel free to take a browse of our website www.velbrooklegal.com.au to get an idea of what we do and the kind of firm we are.

We are in the process of redeveloping our website and as such, so please don't adhere to the design principles of the current site- impress us with your originality!

On top of any editable formats, your final submissions must include a .pdf copy.
The same design will need to be presented in two dimensions:

- 154mm x 118mm (B1/B2 Half Page);
- 175mm x 113mm (B4 Half Page).

[For more information refer to attached Pdf.]

We have attached for you a few examples of other firms' designs (Sample1,2,3). These are by no means good, or what we're after, it's just to provide you with an idea of what sort of advertisements go into the service directory.

Hi all,

We want to emphasise that a priority of the design is that it must look:
• Professional
• Sophisticated
Please do not hesitate to use completely different colour schemes to the ones that are on our website- as we have said, our website will change in the near future, so cohesion between the current project and the website is not necessary!

Thanks!

Thank you for your submissions so far. There are some great ideas hidden in there. 

An issue we are having is that most of you are conforming to the same understanding of what it should look like. Remember that there is NO NEED to be bound by the image of firm as is. That is, feel free to use a different colour logo.

For inspiration, we relate well to the design aesthetics of: http://www.tinfernstudio.co.uk/

Look forward to seeing your 'out of the box' submissions. 

Reason: We've received a large amount of fantastic designs. However, what we're really looking for is something original. Please feel free to think outside the box (the final design doesn't need to look like a print ad), and construct a design that is completely incongruous with our website! While we do appreciate a minimalistic design, we have yet to receive something that really grabs your attention with its visuals. We're not sure but this may or may not be achieved with a full colour design. Thanks for all your submissions- they all have some features that really click with us. We look forward to the next wave of submissions!

Target Market(s)

We have various target markets, including mainly families, elderly people, blue collar workers.

These are individuals who are looking for assistance. They feel helpless or wronged.

Keep in mind that the people accessing these are those who prefer going to a printed directory rather than using a google search.

Industry/Entity Type

Law Firm

Font styles to use
Serif
Sans Serif

Requirements
Must have
• - Our name 'Velbrook Compensation Lawyers'
- Our logo (attached as logo.eps, logo.png, and logo.tif)
- Must include phone number as 1300 XXX XXX (this must be prominent)
- Must include the following service areas in these words: Motor vehicle claims, medical claims, superannuation claims, Workplace claims, negligence claims
- Our email address: info@velbrooklegal.com.au
- Our website address: www.velbrooklegal.com.au
- The following catchphrases: '98% success rate', and 'No win no fee' in those words
- Our location '412 Carvel Lane, Smithville, SYDNEY'
- For sizing dimensions, we need one in 154mm x 118mm and also a design in 175mm x 113mm (B4 Half Page) [refer to pdf attached]
Nice to have
• - Text indicating free initial consulatation
- Professional colour scheme
- As our website will be changed, do not worry about making the advertisement cohesive with our website design
- We want the design to be modern, but still professional
- Clean typeface
- No gradient colour scheme
- When designing, if you are looking to place more text onto the advertisement, these may be some considerations (feel free to change the wording): Accredited specialists, home and hospital visits

```html
<!DOCTYPE html>
<html lang="en">
<head>
<meta charset="utf-8">
<title>Velbrook Compensation Lawyers – Directory Advertisement</title>
<link href="https://fonts.googleapis.com/css2?family=Questrial&display=swap" rel="stylesheet">
<style>
  :root {
    --sand: #e2d388;
    --brand-red: #c8242b;
    --paper: #ffffff;
    --ink: #222222;
    --muted: #8c8c8c;
    --soft-pink: #f4aaa2;
    --fade-mid: #e2957f;
    --fade-end: #f8ebe6;
  }
  * { margin: 0; padding: 0; box-sizing: border-box; }
  html, body {
    width: 1200px; height: 1000px; overflow: hidden;
    background: var(--sand);
    font-family: "Questrial", "Century Gothic", sans-serif;
  }
  .ad {
    position: absolute; left: 54px; top: 73px;
    width: 1103px; height: 844px;
    background: var(--brand-red);
  }
  .ad__sheet {
    position: absolute; left: 36px; top: 0;
    width: 1031px; height: 674px;
    background: var(--paper);
    border-radius: 0 0 72px 72px;
  }
  .ad__content {
    position: absolute; left: 132px; top: 0; width: 767px;
    text-align: center;
  }
  .headline {
    position: absolute; top: 160px; left: -20px; width: calc(100% + 40px);
    font-size: 73px; font-weight: 400; letter-spacing: 0.5px;
    white-space: nowrap; line-height: 1;
    color: var(--brand-red);
  }
  .headline__fade {
    background: linear-gradient(90deg, var(--brand-red) 0%, var(--fade-mid) 25%, var(--fade-end) 100%);
    -webkit-background-clip: text; background-clip: text;
    color: transparent;
  }
  .tagline {
    position: absolute; top: 281px; left: -20px; width: calc(100% + 40px);
    font-size: 33px; color: var(--ink); white-space: nowrap;
  }
  .services {
    position: absolute; top: 354px; left: -20px; width: calc(100% + 40px);
    font-size: 28px; line-height: 31px; color: var(--muted); white-space: nowrap;
  }
  .promise {
    position: absolute; top: 469px; left: -20px; width: calc(100% + 40px);
    font-size: 42px; letter-spacing: 1px; color: var(--ink);
    white-space: nowrap;
  }
  .phone {
    position: absolute; top: 526px; left: -20px; width: calc(100% + 40px);
    white-space: nowrap; line-height: 1;
    display: flex; align-items: baseline; justify-content: center; gap: 18px;
  }
  .phone__label { font-size: 44px; color: var(--ink); }
  .phone__number { font-size: 101px; color: var(--brand-red); letter-spacing: 1px; }

  .footer__mark {
    position: absolute; left: 46px; top: 700px;
  }
  .footer__name {
    position: absolute; left: 178px; top: 716px;
    color: var(--paper); font-weight: 400; line-height: 1;
  }
  .footer__name-main { display: block; font-size: 56px; letter-spacing: 2px; }
  .footer__name-sub { display: block; font-size: 20px; letter-spacing: 4px; margin-top: 10px; }
  .footer__divider {
    position: absolute; left: 551px; top: 716px;
    width: 2px; height: 78px; background: var(--paper);
  }
  .contact {
    position: absolute; left: 593px; top: 711px;
    list-style: none; color: var(--paper);
    font-size: 24px; line-height: 28.5px; letter-spacing: 0.8px;
    white-space: nowrap;
  }
  .contact__prefix { color: var(--soft-pink); }
</style>
</head>
<body>
  <main class="ad">
    <section class="ad__sheet">
      <div class="ad__content">
        <h1 class="headline">velbrookc<span class="headline__fade">ompensation</span></h1>
        <p class="tagline">Some things are so obvious they go without saying.</p>
        <p class="services">Motor vehicle claims, medical claims, superannuation claims,<br>workplace claims, negligence claims.</p>
        <p class="promise">98% SUCCESS RATE. NO WIN NO FEE.</p>
        <p class="phone"><span class="phone__label">PHONE</span><span class="phone__number">1300 835 271</span></p>
      </div>
    </section>

    <svg class="footer__mark" width="106" height="106" viewBox="0 0 106 106" aria-hidden="true">
      <circle cx="53" cy="53" r="52" fill="#ffffff"/>
    </svg>
    <p class="footer__name">
      <span class="footer__name-main">VELBROOK</span>
      <span class="footer__name-sub">COMPENSATION LAWYERS</span>
    </p>
    <div class="footer__divider"></div>
    <ul class="contact">
      <li>412 Carvel Lane, Smithville, SYDNEY</li>
      <li><span class="contact__prefix">e</span> info@velbrooklegal.com.au</li>
      <li><span class="contact__prefix">w</span> www.velbrooklegal.com.au</li>
    </ul>
  </main>
</body>
</html>
```